Online Prescription Eyewear Company Needs a Website

We sell prescription glasses starting at $99 with Free Shipping. We have over 300 different styles and colors.

Our website is under construction and we need an amazing landing page to kick things off. Our brand is called VARNO and our website is called VARNOEYEWEAR.EXAMPLE.

We are a website similar to
kestonhale.example
shoprudyplume.example
Brova.example

We sell prescription glasses starting at $99 with Free Shipping. Options to upgrade to Anti Glare, Blue light Protection, Shadeshift or High Index.

We also have a lens replacement option and will change out old prescription lenses starting at $79 with Free Shipping.

Important!!

We Love the layout of https://tessbrundle.example/ . We are hoping to use Tess Brundle as a templet. The closest page that looks like Tess Brundle will win.

We do not prefer the pink. Substitute the pink with Navy Teal.

We also prefer a better footer than Tess Brundle

The landing page should include, Gender neutral and Colors are Black, White, Gray, Navy Teal

We prefer a Simple, Clean Look.

The Header should be similar to kestonhale.example

The Landing page look very similar to Tess Brundle with large banner with quad banner below to follow.

We need better footer. Here are the menu items for footer.

PRODUCTS
All Frames
Mens Frames
Womens Frames
Best Sellers
New Arrivals

ORDER
Single Vision Lenses
Blue Light Blocking Computer Lenses
High Index Lenses
Shadeshift Lenses
Reading Lenses

INFORMATION
Track Order
About Us
Contact Us
Returns
Warranty
FAQ

Target Market(s)

20-40 yo Male/Female wears glasses

Industry/Entity Type

Eyewear

Number of Pages Required

1 page

Font styles to use
Sans Serif

Colors
333333
5c5c5c
919191
b2b2b2
dfdfdf
f5f5f5
1b1b1b
474747
3276b5

Requirements
Must have
• The Landing page look very similar to Tess Brundle.
• Substitute the pink secondary color for Navy Teal
• Should have main Banner with Person wearing glasses. Then the quad banner below should highlight the box with glasses, glasses, etc.
Nice to have
• i have a pixel vault account, so if you find some awesome pictures I can purchase them if they fit in the site.

```html
<!DOCTYPE html>
<html lang="en">
<head>
<meta charset="utf-8">
<title>VARNO Eyewear</title>
<link rel="stylesheet" href="https://fonts.googleapis.com/css2?family=Merriweather:wght@400;700&family=Lato:wght@400;700&display=swap">
<style>
:root{
  --ink:#1b1b1b;
  --text:#333333;
  --mid:#474747;
  --soft:#5c5c5c;
  --muted:#919191;
  --line:#b2b2b2;
  --pale:#dfdfdf;
  --paper:#f5f5f5;
  --white:#ffffff;
  --accent:#3276b5;
  --star:#f5a623;
  --teal:#1f4e5f;
}
*{box-sizing:border-box;margin:0;padding:0}
html,body{width:1200px;height:4409px;overflow:hidden}
body{position:relative;background:var(--white);font-family:'Lato',sans-serif;color:var(--text)}
.abs{position:absolute}
.serif{font-family:'Merriweather',serif}

/* header */
.site-header{left:0;top:0;width:1200px;height:106px;background:var(--white)}
.brand{left:97px;top:30px;font-size:38px;letter-spacing:6px;font-weight:400;color:var(--ink)}
.main-nav{left:316px;top:46px;display:flex;gap:22px;font-size:14px;color:var(--ink);letter-spacing:.3px}
.util-nav{right:110px;top:46px;display:flex;gap:18px;align-items:center;font-size:14px;color:var(--ink)}
.util-nav .sep{width:1px;height:22px;background:var(--line)}
.util-nav svg{display:block}

/* hero */
.hero{left:0;top:106px;width:1200px;height:664px;background:var(--paper)}
.hero-photo{right:0;top:0;width:600px;height:664px;background:linear-gradient(160deg,#f0efed 0%,#e7e4e0 45%,#4fa9c9 75%,#3c97b8 100%)}
.hero-title{left:118px;top:150px;font-size:56px;line-height:74px;font-weight:700;color:var(--ink)}
.hero-sub{left:118px;top:318px;font-size:20px;line-height:32px;color:var(--ink)}
.btn-outline{border:2px solid var(--mid);background:transparent;color:var(--ink);font-size:18px;letter-spacing:.5px;display:flex;align-items:center;justify-content:center}
.hero-btn{left:115px;top:440px;width:256px;height:64px}

/* quad banners */
.tile{width:483px;height:333px;overflow:hidden}
.tile-art{position:absolute;inset:0}
.tile-label{position:absolute;left:0;bottom:0;width:100%;height:52px;background:rgba(223,223,223,.85);display:flex;align-items:center;justify-content:center;font-size:18px;letter-spacing:.5px;text-decoration:underline;color:var(--ink)}
.t1{left:99px;top:823px}
.t2{left:618px;top:823px}
.t3{left:99px;top:1190px}
.t4{left:618px;top:1190px}

/* about */
.about{left:0;top:1576px;width:1200px;height:614px;background:var(--paper)}
.about-photo{left:0;top:0;width:676px;height:614px;background:linear-gradient(120deg,#d9d6d2 0%,#bdb7b0 40%,#efeeec 70%,#e4e2df 100%)}
.about-title{left:753px;top:135px;font-size:48px;font-weight:400;color:var(--ink)}
.about-copy{left:753px;top:212px;width:360px;font-size:16px;line-height:24px;color:var(--mid)}
.about-btn{left:810px;top:373px;width:170px;height:56px;font-size:16px}

/* testimonials */
.section-title{width:1200px;left:0;text-align:center;font-size:46px;color:var(--ink)}
.testi-title{top:2283px}
.review{width:420px;text-align:center}
.review .stars{display:flex;justify-content:center;gap:6px}
.review h3{margin-top:16px;font-size:18px;font-weight:700;color:var(--ink);letter-spacing:.5px}
.review p{margin-top:20px;font-size:16px;line-height:26px;color:var(--soft)}
.review .avatar{width:72px;height:72px;border-radius:50%;margin:34px auto 0;background:linear-gradient(180deg,#d8c6b3,#a88d74)}
.review .name{margin-top:22px;font-size:17px;font-weight:700;color:var(--mid)}
.r1{left:137px;top:2400px}
.r2{left:643px;top:2400px}
.arrow{top:2526px}
.arrow-l{left:60px}
.arrow-r{left:1108px}
.dots{left:0;top:2810px;width:1200px;display:flex;justify-content:center;gap:9px}
.dots span{width:10px;height:10px;border-radius:50%;background:var(--pale)}
.dots span.on{background:var(--accent)}

/* social gallery */
.gallery-title{top:3008px}
.gallery-sub{left:0;top:3096px;width:1200px;text-align:center;font-size:22px;color:var(--mid)}
.shot{overflow:hidden}
.g1{left:0;top:3175px;width:256px;height:271px;background:linear-gradient(150deg,#c4302b,#efd8cf 50%,#2b2b2b)}
.g2{left:262px;top:3175px;width:255px;height:271px;background:linear-gradient(150deg,#e9e7e4,#8c7d70 60%,#dedbd7)}
.g3{left:523px;top:3175px;width:250px;height:271px;background:linear-gradient(150deg,#f3f1ee,#a57c5b 55%,#c6d4e2)}
.g4{left:779px;top:3175px;width:421px;height:544px;background:linear-gradient(160deg,#7b4a33,#a7806a 35%,#5f8fc4 75%,#4a79ad)}
.g5{left:0;top:3452px;width:479px;height:267px;background:linear-gradient(120deg,#6b6f78,#262a33 45%,#8a5d4e 70%,#b69782)}
.g6{left:485px;top:3452px;width:288px;height:267px;background:linear-gradient(150deg,#1d2b3b,#4a5a6b 50%,#8e7766)}

/* newsletter + footer */
.closing{left:0;top:3740px;width:1200px;height:669px;background:linear-gradient(160deg,#cfcac4,#bab4ad 40%,#d6d2cd 70%,#c4bfb9)}
.closing-veil{left:0;top:3740px;width:1200px;height:669px;background:rgba(245,245,245,.82)}
.news-title{left:0;top:3870px;width:1200px;text-align:center;font-size:38px;color:var(--mid)}
.news-sub{left:0;top:3944px;width:1200px;text-align:center;font-size:20px;color:var(--mid)}
.news-input{left:262px;top:4022px;width:488px;height:46px;background:var(--white);border:1px solid var(--pale);padding-left:22px;display:flex;align-items:center;font-size:15px;color:var(--muted)}
.news-btn{left:779px;top:4022px;width:157px;height:46px;background:var(--accent);color:var(--white);font-size:16px;font-weight:700;display:flex;align-items:center;justify-content:center;letter-spacing:.5px}
.footer-brand{left:156px;top:4140px;font-size:40px;letter-spacing:6px;color:var(--ink)}
.footer-col{top:4144px;font-size:12px;color:var(--soft)}
.footer-col h4{font-size:12px;font-weight:700;color:var(--ink);letter-spacing:.5px;margin-bottom:10px}
.footer-col li{list-style:none;line-height:22px}
.c1{left:509px}
.c2{left:676px}
.c3{left:932px}
.copyright{left:156px;top:4362px;font-size:12px;color:var(--muted)}
</style>
</head>
<body>

<header class="site-header abs">
  <div class="brand abs">VARNO</div>
  <nav class="main-nav abs"><span>EYEGLASSES</span><span>SUNGLASSES</span><span>HOME TRY-ON</span><span>LOCATIONS</span></nav>
  <div class="util-nav abs">
    <svg width="18" height="18" viewBox="0 0 18 18" aria-hidden="true"><circle cx="7.5" cy="7.5" r="5.5" fill="none" stroke="#1b1b1b" stroke-width="1.6"/><line x1="11.5" y1="11.5" x2="16" y2="16" stroke="#1b1b1b" stroke-width="1.6"/></svg>
    <span>SEARCH</span><span class="sep"></span><span>HELP</span><span>SIGN IN</span>
    <svg width="18" height="20" viewBox="0 0 18 20" aria-hidden="true"><path d="M2 6h14l-1 13H3z" fill="none" stroke="#1b1b1b" stroke-width="1.5"/><path d="M6 6V4a3 3 0 0 1 6 0v2" fill="none" stroke="#1b1b1b" stroke-width="1.5"/></svg>
  </div>
</header>

<section class="hero abs">
  <div class="hero-photo abs" role="img" aria-label="Woman in a blue top wearing white-framed sunglasses"></div>
  <h1 class="hero-title abs serif">Wear Your<br>Stylish Glasses</h1>
  <p class="hero-sub abs">We sell prescription glasses starting at $99<br>with <strong>FREE SHIPPING</strong></p>
  <div class="hero-btn btn-outline abs">SHOP NOW</div>
</section>

<a class="tile t1 abs">
  <div class="tile-art" role="img" aria-label="Man in a dark blazer wearing glasses" style="background:linear-gradient(150deg,#e6e4e1,#b7aa9c 45%,#2f3542 80%)"></div>
  <span class="tile-label">MEN FRAMES</span>
</a>
<a class="tile t2 abs">
  <div class="tile-art" role="img" aria-label="Woman with curly hair wearing glasses" style="background:linear-gradient(150deg,#d9d7d4,#6b4a37 45%,#c8603f 85%)"></div>
  <span class="tile-label">WOMEN FRAMES</span>
</a>
<a class="tile t3 abs">
  <div class="tile-art" role="img" aria-label="Glasses with black cases on a teal and pale background" style="background:linear-gradient(120deg,#1f4e5f 0%,#1f4e5f 22%,#c9d9dc 22%,#c9d9dc 100%)"></div>
  <span class="tile-label">OUR BESTSELLERS</span>
</a>
<a class="tile t4 abs">
  <div class="tile-art" role="img" aria-label="Three pairs of eyeglass frames on a light surface" style="background:linear-gradient(150deg,#f3f2f1,#d9d5cf 50%,#f5f5f5)"></div>
  <span class="tile-label">NEW ARRIVALS</span>
</a>

<section class="about abs">
  <div class="about-photo abs" role="img" aria-label="Smiling man and woman wearing glasses in a bright office"></div>
  <h2 class="about-title abs serif">About Varno</h2>
  <p class="about-copy abs">Lorem ipsum dolor sit amet, consectetur adipiscing elit. Suspendisse convallis fringilla velit eu convallis. Proin cursus fringilla est in vulputate. Ut eu dolor eu risus rutrum dictum. Etiam molestie semper urna.</p>
  <div class="about-btn btn-outline abs">LEARN MORE</div>
</section>

<h2 class="section-title testi-title abs serif">Client Testimonial</h2>

<svg class="arrow arrow-l abs" width="28" height="40" viewBox="0 0 28 40" aria-hidden="true"><polyline points="20,6 8,20 20,34" fill="none" stroke="#b2b2b2" stroke-width="3"/></svg>
<svg class="arrow arrow-r abs" width="28" height="40" viewBox="0 0 28 40" aria-hidden="true"><polyline points="8,6 20,20 8,34" fill="none" stroke="#3276b5" stroke-width="3"/></svg>

<div class="review r1 abs">
  <div class="stars">
    <svg width="26" height="25" viewBox="0 0 24 23"><polygon points="12,1 15,8.5 23,9 17,14.3 19,22 12,17.8 5,22 7,14.3 1,9 9,8.5" fill="#f5a623"/></svg>
    <svg width="26" height="25" viewBox="0 0 24 23"><polygon points="12,1 15,8.5 23,9 17,14.3 19,22 12,17.8 5,22 7,14.3 1,9 9,8.5" fill="#f5a623"/></svg>
    <svg width="26" height="25" viewBox="0 0 24 23"><polygon points="12,1 15,8.5 23,9 17,14.3 19,22 12,17.8 5,22 7,14.3 1,9 9,8.5" fill="#f5a623"/></svg>
    <svg width="26" height="25" viewBox="0 0 24 23"><polygon points="12,1 15,8.5 23,9 17,14.3 19,22 12,17.8 5,22 7,14.3 1,9 9,8.5" fill="#f5a623"/></svg>
    <svg width="26" height="25" viewBox="0 0 24 23"><polygon points="12,1 15,8.5 23,9 17,14.3 19,22 12,17.8 5,22 7,14.3 1,9 9,8.5" fill="#f5a623"/></svg>
  </div>
  <h3>EXCELLENT SERVICE</h3>
  <p>"Lorem ipsum dolor sit amet, consectetur adipiscing. Suspendisse convallis fringilla velit eu convallis, cursus fringilla est in vulputate. Ut eu dolor eu risus rutrum dictum. Etiam molestie semper urna."</p>
  <div class="avatar" role="img" aria-label="Portrait of the reviewer"></div>
  <div class="name">Maren T. Holloway</div>
</div>

<div class="review r2 abs">
  <div class="stars">
    <svg width="26" height="25" viewBox="0 0 24 23"><polygon points="12,1 15,8.5 23,9 17,14.3 19,22 12,17.8 5,22 7,14.3 1,9 9,8.5" fill="#f5a623"/></svg>
    <svg width="26" height="25" viewBox="0 0 24 23"><polygon points="12,1 15,8.5 23,9 17,14.3 19,22 12,17.8 5,22 7,14.3 1,9 9,8.5" fill="#f5a623"/></svg>
    <svg width="26" height="25" viewBox="0 0 24 23"><polygon points="12,1 15,8.5 23,9 17,14.3 19,22 12,17.8 5,22 7,14.3 1,9 9,8.5" fill="#f5a623"/></svg>
    <svg width="26" height="25" viewBox="0 0 24 23"><polygon points="12,1 15,8.5 23,9 17,14.3 19,22 12,17.8 5,22 7,14.3 1,9 9,8.5" fill="#f5a623"/></svg>
    <svg width="26" height="25" viewBox="0 0 24 23"><polygon points="12,1 15,8.5 23,9 17,14.3 19,22 12,17.8 5,22 7,14.3 1,9 9,8.5" fill="#f5a623"/></svg>
  </div>
  <h3>EXCELLENT SERVICE</h3>
  <p>"Lorem ipsum dolor sit amet, consectetur adipiscing. Suspendisse convallis fringilla velit eu convallis, cursus fringilla est in vulputate. Ut eu dolor eu risus rutrum dictum. Etiam molestie semper urna."</p>
  <div class="avatar" role="img" aria-label="Portrait of the reviewer" style="background:linear-gradient(180deg,#9a6b52,#5a3e30)"></div>
  <div class="name">Dorian K. Vale</div>
</div>

<div class="dots abs"><span class="on"></span><span></span><span></span><span></span></div>

<h2 class="section-title gallery-title abs serif">Foloow Us on Picturely</h2>
<p class="gallery-sub abs">Did you loved our products? mention us on social media with <strong>#Varno</strong></p>

<div class="shot g1 abs" role="img" aria-label="Woman in a red beret wearing round glasses"></div>
<div class="shot g2 abs" role="img" aria-label="Bearded man wearing glasses"></div>
<div class="shot g3 abs" role="img" aria-label="Woman wearing sunglasses"></div>
<div class="shot g4 abs" role="img" aria-label="Smiling man in a blue shirt wearing glasses"></div>
<div class="shot g5 abs" role="img" aria-label="Two friends in sunglasses by a brick wall"></div>
<div class="shot g6 abs" role="img" aria-label="Man in a denim jacket wearing glasses"></div>

<div class="closing abs" role="img" aria-label="Faded photo of people wearing glasses"></div>
<div class="closing-veil abs"></div>

<h2 class="news-title abs serif">Subscribe to Our Newsletter</h2>
<p class="news-sub abs">Join the community today and take 10% OFF of your first purchase</p>
<div class="news-input abs">Enter Your Email Address</div>
<div class="news-btn abs">SIGN UP</div>

<footer>
  <div class="footer-brand abs">VARNO</div>
  <div class="footer-col c1 abs">
    <h4>PRODUCTS</h4>
    <ul><li>All Frames</li><li>Mens Frames</li><li>Womens Frames</li><li>Best Sellers</li><li>New Arrivals</li></ul>
  </div>
  <div class="footer-col c2 abs">
    <h4>ORDER</h4>
    <ul><li>Single Vision Lenses</li><li>Blue Light Blocking Computer Lenses</li><li>High Index Lenses</li><li>Shadeshift Lenses</li><li>Reading Lenses</li></ul>
  </div>
  <div class="footer-col c3 abs">
    <h4>INFORMATION</h4>
    <ul><li>Track Order</li><li>About Us</li><li>Contact Us</li><li>Returns</li><li>Warranty</li><li>FAQ</li></ul>
  </div>
  <div class="copyright abs">© 2019 by Varno. All rights reserved.</div>
</footer>

</body>
</html>
```